Bluepeak Comfort HVAC Card

Sale, Install, Maintenance Commercial Vent Hood, Ice Machine & Refrigeration
Air Conditioning Heating & Cooling

Industry/Entity Type

Air Conditioning

Contact Information for Business Card

Bluepeak Comfort
2437 Marisol Ave.
Del Rio Tx, 78852
Ph. (830) 555-0172 Tomas J. Villareal Owner
Ph. (830) 555-0438 Hugo Espinoza Tec.
E-mail. bluepeakcomfort2437@mailnest.example

```html
<!DOCTYPE html>
<html lang="en">
<head>
<meta charset="utf-8">
<title>Bluepeak Comfort – Business Card</title>
<link rel="stylesheet" href="https://fonts.googleapis.com/css2?family=Cinzel:wght@400&family=Open+Sans:wght@400;600&display=swap">
<style>
  :root {
    --backdrop: #2a2623;
    --card: #141414;
    --card-back: #111111;
    --ink: #ffffff;
    --ink-soft: #d6d6d6;
    --divider: #3a3a3a;
    --silver: #a9a9a9;
  }
  * { margin: 0; padding: 0; box-sizing: border-box; }
  html, body {
    width: 1200px;
    height: 844px;
    overflow: hidden;
    background: var(--backdrop);
  }
  .canvas {
    position: relative;
    width: 1200px;
    height: 844px;
    display: flex;
    align-items: center;
    justify-content: center;
    gap: 40px;
  }
  .card {
    position: relative;
    width: 520px;
    height: 298px;
    border-radius: 3px;
    overflow: hidden;
  }
  .card--front { background: var(--card); }
  .card--back  { background: var(--card-back); }

  /* Front side */
  .brand-block {
    position: absolute;
    left: 36px;
    top: 0;
    width: 180px;
    height: 100%;
    display: flex;
    flex-direction: column;
    justify-content: center;
    gap: 14px;
  }
  .brand-block__square {
    width: 40px;
    height: 40px;
    background: var(--ink);
  }
  .brand-block__name {
    font-family: "Open Sans", sans-serif;
    font-weight: 600;
    font-size: 28px;
    line-height: 1.1;
    color: var(--ink);
  }
  .card__divider {
    position: absolute;
    left: 234px;
    top: 44px;
    width: 1px;
    height: 210px;
    background: var(--divider);
  }
  .contact {
    position: absolute;
    left: 254px;
    top: 44px;
    width: 256px;
    font-family: "Open Sans", sans-serif;
    color: var(--ink-soft);
    font-size: 11.5px;
    line-height: 1.4;
  }
  .contact__name {
    font-weight: 600;
    font-size: 19px;
    color: var(--ink);
    line-height: 1.2;
  }
  .contact__role { font-size: 12px; margin-bottom: 14px; }
  .contact__lines { list-style: none; margin-bottom: 12px; }
  .contact__lines li { white-space: nowrap; }
</style>
</head>
<body>
<main class="canvas">
  <section class="card card--front" aria-label="Business card front">
    <div class="brand-block">
      <span class="brand-block__square"></span>
      <span class="brand-block__name">Bluepeak Comfort</span>
    </div>
    <span class="card__divider"></span>
    <div class="contact">
      <p class="contact__name">Tomas J. Villareal</p>
      <p class="contact__role">Owner</p>
      <ul class="contact__lines">
        <li>T: (830) 555-0172</li>
        <li>Hugo Espinoza, Tec.: (830) 555-0438</li>
        <li>E: bluepeakcomfort2437@mailnest.example</li>
      </ul>
      <p class="contact__address">2437 Marisol Ave.<br>Del Rio Tx, 78852</p>
    </div>
  </section>

  <section class="card card--back" aria-label="Business card back">
    <div class="wordmark">
      <span class="wordmark__circle"></span>
      <span class="wordmark__name">Bluepeak Comfort</span>
    </div>
  </section>
</main>
<style>
  .wordmark {
    position: absolute;
    inset: 0;
    display: flex;
    flex-direction: column;
    align-items: center;
    justify-content: center;
    gap: 34px;
  }
  .wordmark__circle {
    width: 64px;
    height: 64px;
    border-radius: 50%;
    background: var(--silver);
  }
  .wordmark__name {
    font-family: "Cinzel", serif;
    font-weight: 400;
    font-size: 30px;
    letter-spacing: 1px;
    color: var(--silver);
  }
</style>
</body>
</html>
```